Marlowe Holdings LLC - Business Cards

Need the following information on the cards:

Name: Dean R Vossler
Title: Chief Executive Manager

Business address:
412 N Ridgeview Lane #118
Brookfield Glen, Il 60412

Phone: (630) 555-0148 - Business
KPV FFL license number: 5-21-xxx-xx-xx-04519
Email: dean.vossler@marloweholdingsffl.com

Target Market(s)

Firearm owners

Industry/Entity Type

Firearms industry,

Contact Information for Business Card

Contact number, name and title, web page address, email, business address and kpv license number,

Requirements
Must have
• Name, title, business address, phone numbers, KPV license numbers, web page address and email address.
Nice to have
• Cellphone number,

```html
<!DOCTYPE html>
<html lang="en">
<head>
<meta charset="utf-8">
<title>Marlowe Holdings LLC – Business Cards</title>
<link rel="stylesheet" href="https://fonts.googleapis.com/css2?family=Roboto+Slab:wght@400;700&display=swap">
<style>
  :root {
    --page: #e6e6e4;
    --card: #ffffff;
    --ink: #2b2b2b;
    --muted: #444444;
    --red: #d4161e;
    --panel: #231f20;
    --rule: #3a3a3a;
  }
  * { box-sizing: border-box; margin: 0; padding: 0; }
  html, body { width: 1200px; height: 1200px; overflow: hidden; }
  body {
    background: var(--page);
    font-family: "Roboto Slab", Georgia, serif;
    color: var(--ink);
    display: flex;
    flex-direction: column;
    align-items: center;
    justify-content: center;
    gap: 60px;
  }
  .card {
    width: 900px;
    height: 514px;
    background: var(--card);
    position: relative;
    overflow: hidden;
    box-shadow: 0 10px 30px rgba(0,0,0,0.18);
    display: flex;
  }
  .brand {
    display: flex;
    flex-direction: column;
    align-items: center;
    justify-content: center;
    gap: 18px;
    text-align: center;
  }
  .brand-mark {
    width: 110px;
    height: 110px;
    border-radius: 50%;
    border: 4px solid var(--red);
  }
  .brand-name {
    font-weight: 700;
    font-size: 30px;
    line-height: 1.15;
    color: var(--red);
    letter-spacing: 0.5px;
  }
  /* front */
  .card-front .brand { width: 48%; padding-left: 20px; }
  .front-art {
    position: absolute;
    right: 0; top: 0;
    width: 52%;
    height: 100%;
    background: var(--panel);
  }
  .front-art .art-fill {
    position: absolute;
    left: -60px; top: 90px;
    width: calc(100% + 60px); height: 424px;
    border-radius: 200px 0 0 0;
    background: linear-gradient(135deg, #2c2627 0%, #1a1718 60%, #3a1a1b 100%);
    border-top: 5px solid var(--red);
    border-left: 5px solid var(--red);
  }
  /* back */
  .card-back .brand { width: 40%; }
  .divider {
    width: 2px;
    background: var(--rule);
    align-self: stretch;
  }
  .details {
    flex: 1;
    padding: 56px 40px 0 44px;
  }
  .person-name {
    font-weight: 700;
    font-size: 38px;
    color: var(--red);
    line-height: 1.05;
  }
  .person-title {
    font-size: 19px;
    color: var(--muted);
    margin-bottom: 40px;
  }
  .contact-list { list-style: none; display: flex; flex-direction: column; gap: 22px; }
  .contact-item {
    display: flex;
    gap: 14px;
    align-items: flex-start;
    font-size: 18px;
    line-height: 1.3;
    color: var(--ink);
  }
  .contact-item svg { width: 20px; height: 20px; flex: none; margin-top: 2px; fill: var(--red); }
  .license { margin-top: 50px; font-size: 18px; line-height: 1.35; }
  .license-label { color: var(--red); }
</style>
</head>
<body>
  <section class="card card-front">
    <div class="brand">
      <div class="brand-mark"></div>
      <div class="brand-name">Marlowe<br>Holdings LLC</div>
    </div>
    <div class="front-art">
      <div class="art-fill" role="img" aria-label="Illustration of a black shepherd dog outlined in red, facing left"></div>
    </div>
  </section>

  <section class="card card-back">
    <div class="brand">
      <div class="brand-mark"></div>
      <div class="brand-name">Marlowe<br>Holdings LLC</div>
    </div>
    <div class="divider"></div>
    <div class="details">
      <h1 class="person-name">Dean R Vossler</h1>
      <p class="person-title">Chief Executive Manager</p>
      <ul class="contact-list">
        <li class="contact-item">
          <svg viewBox="0 0 24 24" aria-hidden="true"><path d="M6.6 10.8a15.1 15.1 0 0 0 6.6 6.6l2.2-2.2a1 1 0 0 1 1-.25 11.4 11.4 0 0 0 3.6.57 1 1 0 0 1 1 1V20a1 1 0 0 1-1 1A17 17 0 0 1 3 4a1 1 0 0 1 1-1h3.5a1 1 0 0 1 1 1c0 1.25.2 2.45.57 3.57a1 1 0 0 1-.25 1z"/></svg>
          <span>(630) 555-0148 - Business</span>
        </li>
        <li class="contact-item">
          <svg viewBox="0 0 24 24" aria-hidden="true"><path d="M2 5h20v14H2z"/><path d="M3 6l9 6.3L21 6" stroke="#fff" stroke-width="1.6" fill="none"/></svg>
          <span>dean.vossler@marloweholdingsffl.com</span>
        </li>
        <li class="contact-item">
          <svg viewBox="0 0 24 24" aria-hidden="true"><path d="M12 2a7 7 0 0 0-7 7c0 5.2 7 13 7 13s7-7.8 7-13a7 7 0 0 0-7-7zm0 9.5A2.5 2.5 0 1 1 12 6.5a2.5 2.5 0 0 1 0 5z"/></svg>
          <span>412 N Ridgeview Lane #118<br>Brookfield Glen, Il 60412</span>
        </li>
      </ul>
      <p class="license"><span class="license-label">KPV FFL license number:</span><br>5-21-xxx-xx-xx-04519</p>
    </div>
  </section>
</body>
</html>
```